political election

Elect Ramiro Duval

for

Pellwick School Board Pl. ?

colors used are red, white, and blue

any other graphics are more than welcome.

need this in fine print at bottom

advertising paid for by candidate

Target Market(s)

voters of the school district

Industry/Entity Type

School

Requirements
Must have
• red white and blue and in fine print advertisement paid for by candidate.
Nice to have
• graphics, art

```html
<!DOCTYPE html>
<html lang="en">
<head>
<meta charset="utf-8">
<title>Elect Ramiro Duval – Pellwick School Board</title>
<link rel="stylesheet" href="https://fonts.googleapis.com/css2?family=Archivo:wght@400;900&display=swap">
<style>
  :root {
    --page-bg: #eceae6;
    --campaign-red: #e0232b;
    --campaign-red-dark: #c81c23;
    --campaign-blue: #1f3f86;
    --campaign-blue-deep: #1a3676;
    --paper-white: #ffffff;
    --slot-dark: #1c1c22;
    --ballot-grey: #d9d9d9;
  }
  * { box-sizing: border-box; margin: 0; padding: 0; }
  html, body {
    width: 1200px;
    height: 1000px;
    overflow: hidden;
    background: var(--page-bg);
    font-family: "Archivo", Arial, sans-serif;
  }
  .flyer {
    position: absolute;
    left: 260px;
    top: 40px;
    width: 680px;
    height: 920px;
    background: var(--campaign-blue);
    overflow: hidden;
    box-shadow: 0 10px 30px rgba(0,0,0,0.18);
  }
  .flyer__banner {
    position: absolute;
    left: 0; top: 0;
    width: 100%;
    height: 210px;
    background: radial-gradient(ellipse at 48% 100%, var(--campaign-red) 0%, var(--campaign-red-dark) 100%);
  }
  .flyer__ballot-art {
    position: absolute;
    left: 250px;
    top: 0;
    width: 190px;
    height: 262px;
    background: linear-gradient(180deg, #9a9a9a 0%, var(--ballot-grey) 35%, var(--paper-white) 100%);
  }
  .flyer__slot {
    position: absolute;
    left: 236px;
    top: 270px;
    width: 210px;
    height: 8px;
    border-radius: 3px;
    background: var(--slot-dark);
    box-shadow: 0 1px 0 rgba(255,255,255,0.35);
  }
  .headline {
    position: absolute;
    left: 0;
    top: 292px;
    width: 100%;
    color: var(--paper-white);
    text-shadow: 0 3px 4px rgba(0,0,0,0.3);
  }
  .headline__elect {
    display: flex;
    align-items: center;
    justify-content: center;
    gap: 14px;
    font-weight: 900;
    font-size: 46px;
    letter-spacing: 1px;
    text-transform: uppercase;
  }
  .stars {
    font-size: 16px;
    letter-spacing: 3px;
    font-weight: 400;
    text-shadow: none;
  }
  .headline__name {
    margin: 6px 0 0 168px;
    font-weight: 900;
    font-size: 104px;
    line-height: 0.94;
    letter-spacing: -2px;
    text-transform: uppercase;
  }
  .headline__for {
    margin: 16px 0 0 330px;
    font-weight: 400;
    font-size: 40px;
    text-transform: uppercase;
    text-shadow: none;
  }
  .headline__office {
    position: relative;
    margin: 6px 0 0 168px;
    font-weight: 900;
    font-size: 62px;
    line-height: 0.98;
    text-transform: uppercase;
  }
  .headline__office .stars {
    position: absolute;
    right: 58px;
    top: 78px;
  }
  .fine-print {
    position: absolute;
    left: 0;
    top: 838px;
    width: 100%;
    display: flex;
    justify-content: center;
    align-items: center;
    gap: 14px;
    color: var(--paper-white);
    font-size: 15px;
    letter-spacing: 0.5px;
  }
</style>
</head>
<body>
  <main class="flyer">
    <div class="flyer__banner"></div>
    <div class="flyer__ballot-art" role="img" aria-label="Photograph of a hand dropping a white ballot into a ballot box slot"></div>
    <div class="flyer__slot"></div>

    <section class="headline">
      <p class="headline__elect"><span class="stars">★★★★★</span>Elect<span class="stars">★★★★★</span></p>
      <h1 class="headline__name">Ramiro<br>Duval</h1>
      <p class="headline__for">for</p>
      <h2 class="headline__office">Pellwick<br>School<br>Board Pl.?<span class="stars">★★★★★</span></h2>
    </section>

    <p class="fine-print"><span class="stars">★★★★★</span>advertising paid for by candidate</p>
  </main>
</body>
</html>
```